website re-design

require to re design my existing website ( www.lunarfoxgrove.example ) to show a corporate image of the company . i also require an advise on the content editorial text . i am currently using pel wimbo for domain registration and website design and publishing .

Target Market(s)

focus on the meddle east market , but visible for worldwide business opportunity

Industry/Entity Type

It Company

Coding

Coded - Design and coding required

Number of Pages Required

5+ page

Requirements
Must have
• --show the brand color when possible ,
• --professional website reflecting the following main key areas :broadcast /media/consultancy services/technology
• --number of pages to be maintained or increased if necessary
• --adaptive design for all PC and mobiles
• --simple to navigate and get the idea quickly
• --landing page with full image and slight movement in the background
Nice to have
• any interactivity with visitors
• font style to be recommended by the designer ( professional test , easy to read )
• more descriptive image and less text
• visitor to know what we do more from graphics , image and video
• landing page to have some motions ( similar to www.harbortwillco.example/ )

```html
<!DOCTYPE html>
<html lang="en">
<head>
<meta charset="utf-8">
<title>Lunar Fox Grove – Broadcast System Solutions</title>
<link href="https://fonts.googleapis.com/css2?family=Raleway:wght@300;400;500;600&family=Open+Sans:wght@400;600&display=swap" rel="stylesheet">
<style>
:root{
  --orange:#f27a1c;
  --orange-dark:#e06a10;
  --ink:#2a2a2a;
  --muted:#666;
  --dark:#1c1d20;
  --darker:#141414;
  --light:#f1f1f1;
  --white:#fff;
}
*{box-sizing:border-box;margin:0;padding:0}
html,body{width:1200px;height:3879px;overflow:hidden}
body{font-family:"Open Sans",Arial,sans-serif;color:var(--ink);background:var(--white);position:relative}
.section{position:absolute;left:0;width:1200px}
.heading{font-family:"Raleway",Arial,sans-serif;font-weight:400;color:var(--orange);text-align:center;font-size:44px;letter-spacing:1px}

/* header */
.site-header{top:0;height:124px;background:var(--white)}
.topbar{position:absolute;top:0;left:0;width:1200px;height:46px;background:var(--white);border-bottom:1px solid #eee}
.topbar-contact{position:absolute;right:70px;top:12px;display:flex;gap:28px;font-size:14px;color:#333}
.topbar-contact span{display:flex;align-items:center;gap:8px}
.brand{position:absolute;left:72px;top:38px;width:114px;height:86px;background:var(--orange);color:var(--white);font-family:"Raleway",Arial,sans-serif;font-weight:600;font-size:19px;line-height:20px;padding:12px 10px}
.main-nav{position:absolute;left:292px;top:74px;display:flex;gap:40px;font-family:"Raleway",Arial,sans-serif;font-weight:500;font-size:16px;color:#333}
.main-nav .active{color:var(--orange)}

/* hero */
.hero{top:124px;height:554px;background:linear-gradient(180deg,#5b4a3b 0%,#3a3029 45%,#8a7a66 78%,#c9bda9 100%)}
.hero-arrow{position:absolute;top:215px;width:46px;height:46px;border:2px solid rgba(255,255,255,.4);border-radius:50%}
.hero-caption{position:absolute;left:0;bottom:0;width:1200px;height:82px;background:rgba(0,0,0,.55);color:var(--white);font-size:19px;line-height:28px;padding:12px 90px}

/* welcome */
.welcome{top:678px;height:576px}
.welcome .heading{margin-top:32px}
.welcome-text{width:930px;margin:18px auto 0;text-align:center;font-size:14px;line-height:25px;color:var(--muted)}
.feature-row{position:absolute;top:258px;left:78px;display:flex;gap:58px}
.feature{width:312px;text-align:center}
.feature .photo{height:189px}
.feature p{margin-top:14px;font-size:17px;line-height:26px;color:#333}

/* services */
.services{top:1254px;height:590px;background:linear-gradient(180deg,#1b2530 0%,#141a22 100%);color:var(--white)}
.services .heading{margin-top:40px}
.services-intro{width:860px;margin:20px auto 0;text-align:center;font-size:14px;line-height:24px;color:#ddd}
.service-row{position:absolute;top:198px;left:78px;display:flex;gap:55px}
.service{width:330px;text-align:center}
.service-icon{width:120px;height:120px;margin:0 auto;border-radius:50%;background:var(--orange);display:flex;align-items:center;justify-content:center}
.service h3{margin-top:20px;font-family:"Raleway",Arial,sans-serif;font-weight:500;font-size:18px;color:var(--orange)}
.service p{margin:8px auto 0;width:300px;font-size:13px;line-height:24px;color:#ddd}
.btn{display:inline-block;background:var(--orange);color:var(--white);font-family:"Raleway",Arial,sans-serif;font-size:18px;text-align:center}
.view-all{position:absolute;left:512px;top:473px;width:176px;height:57px;line-height:57px}

/* employment */
.employment{top:1844px;height:132px;background:var(--orange);color:var(--white)}
.employment-icon{position:absolute;left:78px;top:36px}
.employment h2{position:absolute;left:176px;top:28px;font-family:"Raleway",Arial,sans-serif;font-weight:500;font-size:32px}
.employment p{position:absolute;left:176px;top:74px;font-size:16px}
.send-cv{position:absolute;left:924px;top:38px;width:198px;height:56px;border:2px solid var(--white);text-align:center;line-height:52px;font-family:"Raleway",Arial,sans-serif;font-size:19px}

/* solutions */
.solutions{top:1976px;height:434px}
.solutions .heading{position:absolute;left:78px;top:40px;text-align:left}
.solutions-text{position:absolute;left:78px;top:106px;width:680px;font-size:14px;line-height:24px;color:#444}
.solution-list{position:absolute;left:78px;top:172px;list-style:none;font-size:13.5px;line-height:28.6px;color:#444}
.solution-list li{display:flex;align-items:center;gap:16px}
.solution-list li::before{content:"";width:10px;height:10px;background:var(--orange)}
.solution-screen{position:absolute;left:789px;top:103px;width:331px;height:207px;background:#111;border-radius:6px;padding:10px}
.solution-screen .photo{width:100%;height:100%}

/* news */
.news{top:2410px;height:525px;background:linear-gradient(180deg,#1e2733 0%,#151a20 100%);color:var(--white)}
.news .heading{margin-top:36px}
.news-row{position:absolute;top:132px;left:78px;display:flex;gap:38px}
.news-card{width:322px}
.news-card .photo{height:191px}
.news-card h3{margin-top:22px;font-family:"Raleway",Arial,sans-serif;font-weight:500;font-size:16px;line-height:22px;color:var(--orange)}
.news-card p{margin-top:8px;font-size:13px;line-height:22px;color:#ddd}
.news-card time{display:block;margin-top:4px;font-size:13px;color:var(--orange)}

/* contact */
.contact{top:2935px;height:484px}
.contact .heading{margin-top:36px}
.contact-intro{width:760px;margin:14px auto 0;text-align:center;font-size:14px;line-height:24px;color:#444}
.field{position:absolute;height:50px;border:1px solid #ccc;font-size:13px;color:#666;padding:14px 12px}
.field.focused{border-color:var(--orange);background:#fbf0e8}
.submit{position:absolute;left:528px;top:365px;width:144px;height:54px;line-height:54px}

/* partners */
.partners{top:3419px;height:137px;background:var(--light);display:flex;align-items:center;justify-content:center;gap:44px}
.partner{background:#2b2b2b;opacity:.85}

/* footer */
.site-footer{top:3556px;height:259px;background:var(--darker);color:#ccc;font-size:13px}
.footer-col{position:absolute;top:32px}
.footer-col h4{font-family:"Raleway",Arial,sans-serif;font-weight:600;font-size:15px;color:var(--orange);margin-bottom:14px}
.footer-links{list-style:none;line-height:24px}
.footer-links .current{color:var(--orange)}
.footer-post{display:flex;gap:12px;margin-bottom:14px;width:240px}
.footer-post .thumb{width:52px;height:52px;border-radius:50%;background:#777;flex:none}
.footer-post p{line-height:19px}
.footer-post time{color:var(--orange);font-size:12px}
.touch-line{display:flex;gap:12px;align-items:flex-start;line-height:20px;margin-bottom:8px}
.touch-line b{color:var(--orange);font-weight:600}
.map{position:absolute;left:871px;top:72px;width:249px;height:161px;background:linear-gradient(135deg,#e8e6df,#d6d9d2)}
.bottom-bar{top:3815px;height:64px;background:var(--orange);color:var(--white);font-size:13px}
.bottom-bar p{position:absolute;left:78px;top:22px}
.social{position:absolute;top:22px;width:20px;height:20px;border-radius:50%;background:rgba(255,255,255,.85)}
</style>
</head>
<body>

<header class="section site-header">
  <div class="topbar">
    <div class="topbar-contact">
      <span><svg width="16" height="16" viewBox="0 0 24 24"><path fill="#f27a1c" d="M6.6 10.8a15 15 0 006.6 6.6l2.2-2.2c.3-.3.7-.4 1-.2 1.1.4 2.3.6 3.6.6.6 0 1 .4 1 1V20c0 .6-.4 1-1 1A17 17 0 013 4c0-.6.4-1 1-1h3.5c.6 0 1 .4 1 1 0 1.3.2 2.5.6 3.6.1.3 0 .7-.2 1z"/></svg>000 555 0147</span>
      <span><svg width="18" height="14" viewBox="0 0 18 14"><rect width="18" height="14" rx="1" fill="#f27a1c"/><path d="M1 1l8 6 8-6" stroke="#fff" stroke-width="1.5" fill="none"/></svg>info@lunarfoxgrove.example</span>
    </div>
  </div>
  <div class="brand">LUNAR<br>FOX<br>GROVE</div>
  <nav class="main-nav">
    <span class="active">HOME</span><span>ABOUT</span><span>SERVICES</span><span>SOLUTIONS</span><span>CUSTOMERS</span><span>EMPLOYMENTS</span><span>CONTACT</span>
  </nav>
</header>

<section class="section hero" role="img" aria-label="Desk scene with a monitor showing a wall of video channels, a desk lamp and floating social icons">
  <span class="hero-arrow" style="left:14px"></span>
  <span class="hero-arrow" style="right:14px"></span>
  <p class="hero-caption">20 Years of Experience in Studio and Facility Design , Engineering , Integration and Support of Broadcast , Broadband and Telecommunication Systems .</p>
</section>

<section class="section welcome">
  <h1 class="heading">WELCOME TO LUNAR FOX GROVE</h1>
  <p class="welcome-text">Lunar Fox Grove Provides Broadcast System Solutions and Services to support broadcasters , production house, telecom and satellite operator to achieve their goals of media innovation and operation efficiency through strategic planning and smart investment relying on innovative technologies solutions and professional Services .<br>Lunar Fox Grove is a Technology solution and service provider in the broadcast and telecom media industry . Our objective is to support broadcasters, production house and telecom operators in their migration plan and developing new concepts and</p>
  <div class="feature-row">
    <div class="feature"><div class="photo" role="img" aria-label="Two business consultants reviewing a tablet" style="background:linear-gradient(135deg,#eef1f4,#6b7585 60%,#2c3440)"></div><p>Consultancy and Project<br>Management</p></div>
    <div class="feature"><div class="photo" role="img" aria-label="Engineer standing before a city skyline" style="background:linear-gradient(135deg,#dfe9f0,#9fb3c4 55%,#5f7487)"></div><p>Engineering and Managed<br>Services</p></div>
    <div class="feature"><div class="photo" role="img" aria-label="Broadcast camera operator at a live event" style="background:linear-gradient(135deg,#1a2b5a,#0d1326 60%,#3a4a7a)"></div><p>Innovative Broadcast<br>Technology solutions</p></div>
  </div>
</section>

<section class="section services">
  <h2 class="heading">OUR BEST SERVICES</h2>
  <p class="services-intro">We understand the media and entertainment industry and can help guide you through the technology change. We have extensive real-world experience and practice in the broadcast,</p>
  <div class="service-row">
    <div class="service">
      <div class="service-icon"><svg width="60" height="64" viewBox="0 0 60 64" fill="none" stroke="#fff" stroke-width="3"><path d="M30 24L16 62M30 24l14 38M21 48h18"/><circle cx="30" cy="20" r="4" fill="#fff"/><path d="M20 10a14 14 0 000 20M40 10a14 14 0 010 20M13 4a24 24 0 000 32M47 4a24 24 0 010 32"/></svg></div>
      <h3>Studio and Broadcast Facility Design</h3>
      <p>We understand the media and entertainment industry and can help guide you through the technology change.</p>
    </div>
    <div class="service">
      <div class="service-icon"><svg width="66" height="56" viewBox="0 0 66 56" fill="#fff"><circle cx="33" cy="10" r="7"/><circle cx="12" cy="18" r="6"/><circle cx="54" cy="18" r="6"/><path d="M22 32a11 9 0 0122 0zM2 38a10 8 0 0120 0zM44 38a10 8 0 0120 0z"/><rect x="18" y="36" width="30" height="18" rx="2"/></svg></div>
      <h3>Technology Budget Development</h3>
      <p>We understand the media and entertainment industry and can help guide you through the technology change.</p>
    </div>
    <div class="service">
      <div class="service-icon"><svg width="52" height="62" viewBox="0 0 52 62" fill="none" stroke="#fff" stroke-width="3"><rect x="4" y="6" width="34" height="48" rx="2"/><path d="M11 18h20M11 26h20M11 34h14"/><path d="M44 10l6 6-20 24-8 2 2-8z" fill="#fff"/></svg></div>
      <h3>Develop &amp; Manage RFP's</h3>
      <p>We understand the media and entertainment industry and can help guide you through the technology change.</p>
    </div>
  </div>
  <span class="btn view-all">VIEW ALL</span>
</section>

<section class="section employment">
  <svg class="employment-icon" width="76" height="58" viewBox="0 0 76 58"><rect width="76" height="58" rx="4" fill="#fff"/><path d="M4 6l34 26 34-26" stroke="#f27a1c" stroke-width="4" fill="none"/></svg>
  <h2>EMPLOYMENTS</h2>
  <p>Send your CV to info@lunarfoxgrove.example</p>
  <span class="send-cv">SEND YOUR CV</span>
</section>

<section class="section solutions">
  <h2 class="heading">OUR SOLUTIONS</h2>
  <p class="solutions-text">Our goal is to provide creative and competitive technology solutions that enable to grow your business in a cost effective way and in line with business strategy.Our solutions cover the following categories.</p>
  <ul class="solution-list">
    <li>HBBTV and interactive applications for TV and 2nd screen</li>
    <li>Digital and online media distribution and contribution</li>
    <li>Satellite distribution and contribution compression systems</li>
    <li>End to End OTT platforms</li>
    <li>End to end channel playout and distribution</li>
    <li>Disaster recovery in the cloud</li>
    <li>Augmented reality solutions</li>
  </ul>
  <div class="solution-screen"><div class="photo" role="img" aria-label="Television screen showing a grid of channel thumbnails" style="background:linear-gradient(135deg,#5a6a8a,#b04a5a 45%,#3a7ab0)"></div></div>
</section>

<section class="section news">
  <h2 class="heading">LATEST NEWS</h2>
  <div class="news-row">
    <article class="news-card">
      <div class="photo" role="img" aria-label="Network storage devices" style="background:linear-gradient(135deg,#cfd8e4,#5b7fa8 60%,#2b3d58)"></div>
      <h3>Storage Trends Exploring Objects and Scale-Out NAS</h3>
      <p>Network attached storage, or NAS, continues to expand in acceptance and in capabilities.</p>
      <time>4 Nov 2016</time>
    </article>
    <article class="news-card">
      <div class="photo" role="img" aria-label="Broadcast control room with monitors" style="background:linear-gradient(135deg,#3c4a66,#1e2638 55%,#6a7aa0)"></div>
      <h3>Don't Forget: Deadline to File EAS Form Three Is Nov. 14</h3>
      <p>While most of the U.S. population may experience election fatigue, broadcasters may be forgiven.</p>
      <time>3 Nov 2016</time>
    </article>
    <article class="news-card">
      <div class="photo" role="img" aria-label="Satellite dish against a sunset sky" style="background:linear-gradient(180deg,#e8d6c0,#a08a78 55%,#3a3430)"></div>
      <h3>Bird Conservancy Hails Tower Changes</h3>
      <p>A bird conservation group estimates that approx - imately 750 tall towers in the United States.</p>
      <time>4 Nov 2016</time>
    </article>
  </div>
</section>

<section class="section contact">
  <h2 class="heading">CONTACT US</h2>
  <p class="contact-intro">Lorem Ipsum is simply dummy text of the printing and typesetting industry. Lorem Ipsum has been the industry's standard dummy text ever since the 1500s, when an unknown printer took a</p>
  <div class="field focused" style="left:168px;top:181px;width:285px">Name*</div>
  <div class="field" style="left:463px;top:181px;width:279px">Email*</div>
  <div class="field" style="left:753px;top:181px;width:279px">Phone*</div>
  <div class="field" style="left:168px;top:241px;width:864px;height:108px">Message*</div>
  <span class="btn submit">SUBMIT</span>
</section>

<section class="section partners" aria-label="Partners">
  <span class="partner" style="width:190px;height:54px"></span>
  <span class="partner" style="width:110px;height:60px;border-radius:30px"></span>
  <span class="partner" style="width:160px;height:56px"></span>
  <span class="partner" style="width:190px;height:54px"></span>
  <span class="partner" style="width:70px;height:60px;border-radius:50%"></span>
  <span class="partner" style="width:120px;height:54px"></span>
</section>

<footer class="section site-footer">
  <div class="footer-col" style="left:80px">
    <h4>USEFUL LINKS</h4>
    <ul class="footer-links">
      <li class="current">» Home</li><li>» About</li><li>» Services</li><li>» Solutions</li><li>» Customer</li><li>» Employment</li><li>» Contact</li>
    </ul>
  </div>
  <div class="footer-col" style="left:344px">
    <h4>LATEST NEWS</h4>
    <div class="footer-post"><span class="thumb" role="img" aria-label="Storage article thumbnail"></span><p>Storage Trends Exploring Obj ects and Scale Out NAS<br><time>04.11.2016</time></p></div>
    <div class="footer-post"><span class="thumb" role="img" aria-label="Article thumbnail"></span><p>Lorem Ipsum is simple text of printing and type.<br><time>04.11.2016</time></p></div>
  </div>
  <div class="footer-col" style="left:608px">
    <h4>GET IN TOUCH</h4>
    <div class="touch-line"><svg width="14" height="18" viewBox="0 0 14 18"><path d="M7 0a7 7 0 00-7 7c0 5 7 11 7 11s7-6 7-11a7 7 0 00-7-7z" fill="#f27a1c"/><circle cx="7" cy="7" r="2.5" fill="#141414"/></svg><span><b>LUNAR FOX GROVE</b><br>Harbor Media Park HMP 2, Kell<br>Bld , 2nd floor, PO 000410</span></div>
    <div class="touch-line"><svg width="14" height="14" viewBox="0 0 24 24"><path fill="#f27a1c" d="M6.6 10.8a15 15 0 006.6 6.6l2.2-2.2c.3-.3.7-.4 1-.2 1.1.4 2.3.6 3.6.6.6 0 1 .4 1 1V20c0 .6-.4 1-1 1A17 17 0 013 4c0-.6.4-1 1-1h3.5c.6 0 1 .4 1 1 0 1.3.2 2.5.6 3.6.1.3 0 .7-.2 1z"/></svg>+000-555-01470</div>
    <div class="touch-line"><svg width="14" height="16" viewBox="0 0 14 16"><rect x="1" y="4" width="12" height="11" rx="1" fill="#f27a1c"/><rect x="3" y="0" width="8" height="5" fill="#f27a1c"/></svg>+00-55501-48223</div>
    <div class="touch-line"><svg width="16" height="12" viewBox="0 0 18 14"><rect width="18" height="14" rx="1" fill="#f27a1c"/><path d="M1 1l8 6 8-6" stroke="#141414" stroke-width="1.5" fill="none"/></svg>info@lunarfoxgrove.example</div>
  </div>
  <div class="map" role="img" aria-label="Street map locating the office"><svg width="249" height="161" viewBox="0 0 249 161"><circle cx="70" cy="62" r="9" fill="#e0322a"/><circle cx="70" cy="62" r="3" fill="#fff"/><rect x="84" y="56" width="92" height="20" fill="#fff" stroke="#bbb"/><text x="90" y="70" font-family="Open Sans, Arial, sans-serif" font-size="10" fill="#333">Lunar Fox Grove</text></svg></div>
</footer>

<div class="section bottom-bar">
  <p>LUNAR FOX GROVE - 2016. All Rights Reserved</p>
  <span class="social" style="left:1050px"></span>
  <span class="social" style="left:1080px"></span>
</div>

</body>
</html>
```